Need Trifold Brochure

I need a trifold brochure asap for a project.

Please KNOW how to do a trifold brochure. It should be an 8 1/2 x 11 brochure that is folded in thirds. So there are ultimately 6 sections, 3 on the front and 3 on the back. We need content on both sides, not just one. If you aren't sure what a trifold is please google it. If you submit a design that is not a true trifold it will be immediately eliminated.

All content located on this page
http://harborviewaestheticclinic.example/
All text on this page needs to be incorporated.

Also I attached the 3 before and after images. All 3 of these need to be incorporated preferable\y on the inside of the trifold on per page. The very BACK of the trifold doesn't have to have content, other than maybe the company and phone.

On the outside of the trifold (not the inside) you could do a muted sea or ocean scape as long as the text is legible.

Same colors as website.

Reason: Meant to put 7 days

Target Market(s)

See website. This is for face lifts, so mostly women age 40 and over.

Industry/Entity Type

It Company

Requirements
Must have
• All content located on this page

Also I attached the 3 before and after images. When the trifold is open these could be on each of the 3 pages of the trifold, preferably at the top.

Same colors as website.

```html
<!DOCTYPE html>
<html lang="en">
<head>
<meta charset="utf-8">
<title>The Ageless Facelift – Trifold</title>
<link rel="stylesheet" href="https://fonts.googleapis.com/css2?family=Arimo:wght@400;700&family=Alfa+Slab+One&family=Archivo+Black&display=swap">
<style>
  :root {
    --paper: #ffffff;
    --ink: #111111;
    --sky-panel: #6ecbf2;
    --accent: #f26b2c;
    --deep-blue: #1f3f8a;
    --cream: #fde9cf;
  }
  * { box-sizing: border-box; margin: 0; padding: 0; }
  html, body { width: 926px; height: 1200px; overflow: hidden; background: var(--paper); }
  body { position: relative; font-family: "Arimo", Arial, sans-serif; color: var(--ink); }

  .photo { position: absolute; }
  .photo--dark { background: linear-gradient(160deg, #3f3b3e 0%, #8b7f7c 55%, #b9c0c8 100%); }
  .photo--warm { background: linear-gradient(160deg, #d8c2a4 0%, #e9cdb6 50%, #c7b29a 100%); }
  .photo--clinic { background: linear-gradient(160deg, #cfd3d8 0%, #c9a28a 45%, #e4e6ea 100%); }

  .caption { position: absolute; font-size: 8px; font-weight: 700; white-space: nowrap; }
  .caption--note { font-size: 7px; }
  .caption--note span { font-weight: 400; }

  .offers {
    position: absolute; left: 124px; top: 256px; width: 689px; height: 324px;
    background: var(--sky-panel);
  }
  .offers__title {
    position: absolute; top: 10px; font-size: 17px; font-weight: 700; white-space: nowrap;
    color: var(--accent); font-family: "Archivo Black", Arial, sans-serif; letter-spacing: .2px;
  }
  .offers__list {
    position: absolute; top: 45px; height: 257px; background: var(--paper);
    list-style: none; padding: 8px 10px 0 18px; font-size: 12.5px; font-weight: 700; line-height: 20px;
  }
  .offers__list li { position: relative; }
  .offers__list li::before { content: "•"; position: absolute; left: -14px; }
  .offers__list--left { left: 24px; width: 308px; }
  .offers__list--left li { margin-bottom: 21px; }
  .offers__list--right { left: 363px; width: 308px; padding-top: 10px; }
  .offers__list--right li { margin-bottom: 21px; }
  .indent { display: block; padding-left: 16px; }
  .footnote { position: absolute; left: 363px; top: 283px; font-size: 8px; font-weight: 700; padding-left: 4px; }

  .cover {
    position: absolute; left: 120px; top: 602px; width: 695px; height: 538px; overflow: hidden;
    background: linear-gradient(180deg, #3f6fbf 0%, #7aa7dc 30%, #bcd8ee 50%, #46b2d6 62%, #2aa3cf 80%, #4cc0e2 100%);
  }
  .cover__panel {
    position: absolute; left: 465px; top: 0; width: 230px; height: 538px;
    background: linear-gradient(180deg, rgba(22,44,120,.75) 0%, rgba(30,70,150,.45) 55%, rgba(20,90,160,.4) 100%);
  }
  .cover__title {
    position: absolute; left: 465px; width: 230px; top: 42px; text-align: center; white-space: nowrap;
    font-family: "Alfa Slab One", Georgia, serif; font-size: 47px; line-height: 60px;
    color: var(--cream); -webkit-text-stroke: 2px var(--accent); paint-order: stroke fill;
  }
  .cover__tagline {
    position: absolute; left: 465px; width: 230px; top: 330px; text-align: center;
    color: #fff; font-weight: 700; font-size: 15px; line-height: 26px;
  }
  .cover__seen {
    position: absolute; left: 465px; width: 230px; top: 440px; text-align: center;
    color: #fff; font-family: "Alfa Slab One", Georgia, serif; font-size: 27px; line-height: 44px;
  }
  .cover__label { position: absolute; color: var(--accent); font-weight: 700; font-size: 13px; }
  .cover__patient { position: absolute; left: 55px; top: 445px; font-size: 14px; font-weight: 700; color: #1b1b1b; }
  .cover__note { position: absolute; left: 42px; top: 472px; font-size: 7px; color: #3b4f66; white-space: nowrap; }
  .contact {
    position: absolute; left: 258px; top: 346px; width: 175px; height: 162px;
    background: rgba(235,240,245,.72); text-align: center;
    color: var(--accent); font-weight: 700; font-size: 12.5px; line-height: 22px; padding-top: 16px;
  }
  .contact p + p { margin-top: 14px; }
</style>
</head>
<body>

  <div class="photo photo--dark" style="left:146px;top:67px;width:160px;height:151px" role="img" aria-label="Before photo: patient profile prior to facelift"></div>
  <div class="photo photo--dark" style="left:306px;top:67px;width:160px;height:151px" role="img" aria-label="After photo: patient profile following facelift"></div>
  <span class="caption" style="left:148px;top:221px">BEFORE</span>
  <span class="caption" style="left:440px;top:221px">AFTER</span>
  <span class="caption caption--note" style="left:148px;top:236px">Actual Patient <span>(patient also had optional neck lift procedure)</span></span>

  <div class="photo photo--warm" style="left:476px;top:67px;width:155px;height:151px" role="img" aria-label="Before photo: second patient three-quarter view"></div>
  <div class="photo photo--warm" style="left:631px;top:67px;width:164px;height:151px" role="img" aria-label="After photo: second patient three-quarter view"></div>
  <span class="caption" style="left:478px;top:220px">BEFORE</span>
  <span class="caption" style="left:768px;top:220px">AFTER</span>
  <span class="caption caption--note" style="left:478px;top:235px">Actual Patient <span>(patient also had optional neck lift procedure)</span></span>

  <section class="offers">
    <h2 class="offers__title" style="left:29px">The Ageless Facelift Offers:</h2>
    <h2 class="offers__title" style="left:467px">TOTAL COST $4500</h2>
    <ul class="offers__list offers__list--left">
      <li>No General Anesthesia<br>(but available as an option if desired)</li>
      <li>Decreased Risks</li>
      <li>Less Scars</li>
      <li>Very Quick Recovery*</li>
      <li>Less Bruising and Swelling*</li>
      <li>Short Surgery Time</li>
    </ul>
    <ul class="offers__list offers__list--right">
      <li>Significant Improvement*<span class="indent">No Need for Special Post-Op Care</span></li>
      <li>Free Consultation With Our Staff</li>
      <li>Surgery performed by a fully NBAS Board Certified, internationally known, plastic surgeon.</li>
      <li>Optional add-on procedures can be done<br>&nbsp;&nbsp;at the same time.</li>
    </ul>
    <p class="footnote">* results may vary</p>
  </section>

  <section class="cover">
    <div class="cover__panel"></div>
    <div class="photo photo--clinic" style="left:42px;top:48px;width:144px;height:143px" role="img" aria-label="Before photo: cover patient profile"></div>
    <span class="cover__label" style="left:88px;top:196px">Before</span>
    <div class="photo photo--clinic" style="left:44px;top:238px;width:145px;height:136px" role="img" aria-label="After photo: cover patient profile"></div>
    <span class="cover__label" style="left:96px;top:380px">After</span>
    <p class="cover__patient">Actual Patient</p>
    <p class="cover__note">(patient also had optional neck lift procedure)</p>

    <div class="contact">
      <p>CALL TODAY FOR<br>AN APPOINTMENT</p>
      <p>HARBORVIEW<br>AESTHETIC CLINIC<br>555-214-0387</p>
    </div>

    <h1 class="cover__title">The<br>Ageless<br>Facelift</h1>
    <p class="cover__tagline">The new way to look<br>and feel better fast</p>
    <p class="cover__seen">as seen<br>on TV</p>
  </section>

</body>
</html>
```